Pelmo K3 Van Wrap

Want a professional design to represent our business and services, include our accreditations etc.
Van will be Black with rear swing doors

Requirements
Must have
• Refer to the pdf attachment which will have link to our website for our company info etc
Should not have
• Single rear door! The model has two rear doors on back

```html
<!DOCTYPE html>
<html lang="en">
<head>
<meta charset="utf-8">
<title>Pelmo Fire Systems – Van Wrap</title>
<link rel="stylesheet" href="https://fonts.googleapis.com/css2?family=Michroma&family=Saira:wght@500;600&display=swap">
<style>
  :root {
    --backdrop: #a7a7a7;
    --wrap-black: #1c1c1c;
    --wrap-charcoal: #3a3a3a;
    --wrap-silver: #b9b9b9;
    --wrap-red: #d8232a;
    --wrap-maroon: #5a1218;
    --text-light: #ffffff;
    --text-red: #e8262d;
  }
  html, body {
    margin: 0;
    width: 1200px;
    height: 800px;
    overflow: hidden;
    background: var(--backdrop);
  }
  .wrap-canvas {
    position: relative;
    width: 1200px;
    height: 800px;
  }
  .wrap-art { position: absolute; inset: 0; }
  .brand-name {
    font-family: "Michroma", sans-serif;
    fill: var(--text-light);
  }
  .contact-phone, .contact-email, .contact-web {
    font-family: "Michroma", sans-serif;
  }
  .contact-phone { fill: var(--text-light); font-size: 24px; }
  .contact-email { fill: var(--text-light); font-size: 9.5px; }
  .contact-web { fill: var(--text-red); font-size: 11.5px; }
  .sector-list, .service-line {
    font-family: "Saira", sans-serif;
    font-weight: 500;
    fill: var(--text-light);
  }
  .sector-list { font-size: 10.5px; }
  .service-line { font-size: 10px; }
</style>
</head>
<body>
<main class="wrap-canvas">
  <svg class="wrap-art" viewBox="0 0 1200 800" width="1200" height="800" aria-label="Pelmo Fire Systems van side wrap, flat layout">
    <defs>
      <clipPath id="van-body">
        <path d="M218,515 L220,440 Q228,405 262,394 L340,360 Q402,300 470,272 L905,263 Q946,266 956,292 L985,420 L990,505 L895,505 A58,58 0 0 0 779,505 L395,515 A58,58 0 0 0 279,515 Z"/>
      </clipPath>
      <linearGradient id="upper-dark" x1="0" y1="0" x2="1" y2="0">
        <stop offset="0" stop-color="#4a4a4a"/>
        <stop offset="0.5" stop-color="var(--wrap-black)"/>
        <stop offset="1" stop-color="#2b2b2b"/>
      </linearGradient>
      <linearGradient id="mid-silver" x1="0" y1="0" x2="0" y2="1">
        <stop offset="0" stop-color="#8d8d8d"/>
        <stop offset="1" stop-color="#c8c8c8"/>
      </linearGradient>
      <linearGradient id="rear-maroon" x1="0" y1="0" x2="0" y2="1">
        <stop offset="0" stop-color="#3e0e12"/>
        <stop offset="0.6" stop-color="var(--wrap-maroon)"/>
        <stop offset="1" stop-color="#7a161d"/>
      </linearGradient>
    </defs>

    <g class="wrap-panel" clip-path="url(#van-body)">
      <rect class="base-dark" x="200" y="250" width="820" height="300" fill="url(#upper-dark)"/>
      <path class="silver-sweep" d="M200,440 L760,420 L860,270 L1000,270 L1000,550 L200,550 Z" fill="url(#mid-silver)"/>
      <path class="black-speed-band" d="M250,412 L750,380 L745,395 L420,420 L250,440 Z" fill="var(--wrap-black)"/>
      <path class="red-sill" d="M200,478 L760,462 L1000,462 L1000,550 L200,550 Z" fill="var(--wrap-red)"/>
      <path class="maroon-rear" d="M880,260 L1000,260 L1000,550 L752,550 L752,462 Q790,462 800,420 Z" fill="url(#rear-maroon)"/>
      <path class="silver-stripe" d="M860,260 L878,260 L795,440 Q785,462 752,466 L748,462 Q778,455 785,430 Z" fill="#d9d9d9"/>
      <path class="red-edge" d="M752,466 Q785,458 796,432 L800,432 Q792,464 756,472 L420,480 L420,476 Z" fill="var(--wrap-red)"/>
      <path class="cab-window" d="M362,356 L432,290 L556,284 L556,370 L372,373 Z" fill="#2a2a2a"/>
      <path class="cargo-window" d="M566,283 L902,278 L942,352 L572,362 Z" fill="#000" fill-opacity="0.18"/>
    </g>

    <g class="brand-lockup">
      <rect class="brand-dot" x="598" y="293" width="14" height="14" fill="var(--wrap-red)"/>
      <text class="brand-name" x="622" y="325" font-size="44">PELMO</text>
      <text class="brand-name" x="602" y="352" font-size="19" letter-spacing="6">FIRE SYSTEMS</text>
    </g>

    <g class="sector-list">
      <text x="822" y="370">Sectors:</text>
      <text x="817" y="384">• Critical Environments</text>
      <text x="811" y="398">• Industrial Fire Protection</text>
      <text x="806" y="412">• Data Centres</text>
      <text x="801" y="426">• Commercial Buildings</text>
    </g>

    <g class="contact-block">
      <text class="contact-phone" x="427" y="420">01632 960418</text>
      <text class="contact-email" x="427" y="434">SALES@PELMOFIRESYSTEMS.CO.UK</text>
      <text class="contact-web" x="435" y="458">PELMOFIRESYSTEMS.CO.UK</text>
    </g>

    <text class="service-line" x="420" y="502">Services: Design • Installation • Commissioning • Service &amp; Maintenance</text>
  </svg>
</main>
</body>
</html>
```